One label design for 3 different sizes of honey bottles

Our honey company -- Amber Hollow Apiary -- needs new product labels, integrating our new name and logo. We would like one label design that presents equally well on three different sizes of plastic honey bottles. Designs should include a front and back label.

Keep in mind that we really like our old label. Please submit designs that have a similar color and font scheme as the old label.

In the uploaded files, you will find (1) detailed content instructions for each size label (2 lb, 1 lb, 8 oz), (2) photo of three plastic bottles without labels, (3) *.ai file for the new company logo, and (4) image of old package label.

Requirements
Must have
• Same look and feel as our old label, but with our new name and logo

```html
<!DOCTYPE html>
<html lang="en">
<head>
<meta charset="utf-8">
<title>Amber Hollow Apiary – Honey Labels</title>
<link rel="stylesheet" href="https://fonts.googleapis.com/css2?family=Abril+Fatface&family=Archivo:wght@400;700;800&family=Oswald:wght@400;500&family=Zilla+Slab:wght@400;600&display=swap">
<style>
  :root {
    --cream: #fdecd0;
    --cream-light: #fef4e2;
    --brown: #574a37;
    --gold: #f1d39c;
    --gold-soft: #f6e1b8;
    --amber: #e9a23b;
    --line: #d9b67a;
    --page: #ffffff;
  }
  * { margin: 0; padding: 0; box-sizing: border-box; }
  html, body { width: 766px; height: 1200px; overflow: hidden; background: var(--page); }
  .sheet { position: relative; width: 766px; height: 1200px; }

  .front-label { position: absolute; left: 0; top: 0; width: 400px; height: 1200px; }
  .front-shape { position: absolute; left: 0; top: 0; }
  .tagline {
    position: absolute; left: 48px; width: 304px; top: 396px; text-align: center;
    font-family: "Zilla Slab", serif; font-size: 21px; color: var(--brown); letter-spacing: 0.5px;
  }
  .art { position: absolute; border-radius: 40%; }
  .art-flower-top { left: 76px; top: 338px; width: 158px; height: 112px;
    background: radial-gradient(circle at 50% 40%, var(--gold) 0%, var(--gold-soft) 45%, rgba(253,236,208,0) 72%); }
  .art-blossoms { left: 56px; top: 578px; width: 104px; height: 88px;
    background: radial-gradient(circle, var(--gold-soft) 0%, rgba(253,236,208,0) 70%); }
  .art-dipper { left: 236px; top: 668px; width: 112px; height: 186px;
    background: radial-gradient(ellipse at 50% 45%, var(--gold) 0%, var(--gold-soft) 45%, rgba(253,236,208,0) 72%); }
  .brand-mark {
    position: absolute; left: 60px; width: 280px; top: 660px; text-align: center;
    font-family: "Zilla Slab", serif; font-weight: 600; font-size: 25px; line-height: 1.15; color: var(--brown);
  }
  .net-weight {
    position: absolute; left: 108px; top: 795px; width: 186px; height: 31px;
    background: var(--brown); color: var(--cream);
    font-family: "Oswald", sans-serif; font-size: 17px; line-height: 31px; text-align: center;
  }

  .back-label {
    position: absolute; left: 429px; top: 339px; width: 320px; height: 512px;
    background: var(--cream); box-shadow: 0 2px 4px rgba(0,0,0,0.18);
  }
  .back-frame {
    position: absolute; inset: 5px; border: 1.5px solid var(--brown); border-radius: 4px; overflow: hidden;
  }
  .back-base { position: absolute; left: 0; right: 0; bottom: 0; height: 146px; background: var(--brown); }
  .art-skep { position: absolute; right: 0; top: 2px; width: 88px; height: 104px;
    background: radial-gradient(ellipse at 60% 45%, var(--gold) 0%, var(--gold-soft) 45%, rgba(253,236,208,0) 72%); }
  .art-hive { position: absolute; left: 0; top: 148px; width: 104px; height: 82px;
    background: radial-gradient(ellipse at 45% 55%, var(--gold) 0%, var(--gold-soft) 45%, rgba(253,236,208,0) 72%); }
  .promise {
    position: absolute; left: 16px; right: 16px; top: 44px; text-align: center;
    font-family: "Zilla Slab", serif; font-size: 16px; line-height: 20.5px; color: var(--brown);
  }
  .promise strong { font-weight: 600; }
  .infant-warning {
    position: absolute; right: 10px; top: 190px; text-align: right;
    font-family: "Oswald", sans-serif; font-weight: 500; font-size: 11px; line-height: 14px; color: var(--brown);
  }
  .nutrition {
    position: absolute; left: 11px; top: 227px; width: 282px; height: 162px;
    background: var(--cream-light); border: 1.5px solid var(--brown); padding: 7px 10px;
    font-family: "Archivo", sans-serif; font-size: 9.6px; line-height: 13.6px; color: var(--brown);
  }
  .nutrition h2 { font-family: "Archivo", sans-serif; font-weight: 800; font-size: 16px; line-height: 18px; }
  .nutrition b { font-weight: 800; }
  .nutrition .calories { font-size: 15px; font-weight: 800; }
  .nutrition .footnote { font-size: 6px; line-height: 8px; margin-top: 5px; }
  .address {
    position: absolute; left: 0; right: 0; bottom: 25px; text-align: center;
    font-family: "Zilla Slab", serif; font-size: 15px; line-height: 18.5px; color: var(--cream);
  }
</style>
</head>
<body>
<main class="sheet">

  <section class="front-label" aria-label="Front label">
    <svg class="front-shape" width="400" height="1200" viewBox="0 0 400 1200">
      <defs>
        <linearGradient id="band-fill" x1="0" x2="1" y1="0" y2="0">
          <stop offset="0" stop-color="#f0cf98"/>
          <stop offset="0.5" stop-color="#fbe6c4"/>
          <stop offset="1" stop-color="#f0cf98"/>
        </linearGradient>
      </defs>
      <path class="label-body" d="M78 333 H322 A30 30 0 0 0 352 363 V833 A30 30 0 0 0 322 863 H78 A30 30 0 0 0 48 833 V363 A30 30 0 0 0 78 333 Z"
            fill="var(--cream)" stroke="#e6cfa6" stroke-width="1"/>
      <path class="label-border" d="M84.5 339 H315.5 A36 36 0 0 0 346 368.5 V827.5 A36 36 0 0 0 315.5 857 H84.5 A36 36 0 0 0 54 827.5 V368.5 A36 36 0 0 0 84.5 339 Z"
            fill="none" stroke="var(--brown)" stroke-width="1.2"/>
      <polygon class="band-fold" points="26,440 62,440 62,458 20,458" fill="var(--brown)"/>
      <polygon class="band-fold" points="340,572 383,572 372,592 340,592" fill="var(--brown)"/>
      <rect class="title-band" x="20" y="458" width="363" height="114" fill="url(#band-fill)" stroke="var(--line)" stroke-width="1"/>
      <text class="title-word" x="52" y="552" textLength="298" lengthAdjust="spacingAndGlyphs"
            font-family="'Abril Fatface', serif" font-size="100" fill="var(--brown)">HONEY</text>
    </svg>

    <div class="art art-flower-top" role="img" aria-label="Line drawing of a daisy blossom"></div>
    <p class="tagline">LOCAL · PURE · RAW</p>
    <div class="art art-blossoms" role="img" aria-label="Line drawing of small blossoms"></div>
    <div class="art art-dipper" role="img" aria-label="Line drawing of a honey dipper dripping honey"></div>
    <p class="brand-mark">Amber Hollow<br>Apiary</p>
    <p class="net-weight">Net Wt. 2 LB (907 g)</p>
  </section>

  <section class="back-label" aria-label="Back label">
    <div class="back-frame">
      <div class="back-base"></div>
      <div class="art-skep" role="img" aria-label="Line drawing of a straw beehive"></div>
      <div class="art-hive" role="img" aria-label="Line drawing of a wooden bee house"></div>
      <p class="promise"><strong>Amber Hollow Apiary</strong> promises<br>100% pure honey, never<br>pasteurized, and sourced<br>exclusively from beehives we<br>keep near Cedar Run,<br>West Virginia.</p>
      <p class="infant-warning">DO NOT FEED HONEY TO INFANTS<br>UNDER ONE YEAR OLD</p>
      <div class="nutrition">
        <h2>Nutrition Facts</h2>
        <p>Servings: 43, <b>Serv. size: 1 Tbsp (21g)</b>,</p>
        <p>Amount per serving: <b>Calories</b> <span class="calories">60,</span> <b>Total Fat</b> 0g (0% DV), Sat. Fat 0g (0% DV), Trans Fat 0g, <b>Cholest.</b> 0mg (0% DV), <b>Sodium</b> 0mg (0% DV), <b>Total Carb.</b> 17g (6% DV), Fiber 0g (0% DV), Total Sugars 17g (34% DV*), <b>Protein</b> 0g, Vit. D (0% DV), Calcium (0% DV), Iron (0% DV), Potas (0% DV).</p>
        <p class="footnote">* One serving adds 17g of sugar to your diet and represents 34% of the Daily Value for Added Sugars.</p>
      </div>
      <p class="address">Amber Hollow Apiary<br>57 Linden Hollow Road<br>Cedar Run, WV 25499<br>www.amberhollowapiary.com</p>
    </div>
  </section>

</main>
</body>
</html>
```